HIGH-END ANTI AGING START-UP NEEDS DOCUMENT/LETTERHEAD DESIGN!!!!

We are a high end anti-aging and health start-up catering to clients in Stamford and NYC. We just did a logo redesign and are now looking for a letter head design that we can use IN GOOGLE DOCS for marwickcaregroup.example clients. We are REALLY EXCITED to see what you can show us!!!!!!!! We need something sophisticated and MODERN! Thanks so much!

Target Market(s)

High end, boutique medical clients. Our clientele is fairly high profile and we need a sleek, sophisticated letter head to put on all of our marketing materials and medical forms as well.

Industry/Entity Type

Medical

Font styles to use
Serif
Sans Serif

Colors
0255a3
ffffff
00a990
1b1b1b
919191

Requirements
Must have
• Must have the logo and "Marwick Care Group" written somewhere. Must have our URL www.marwickcaregroup.example.
Nice to have
• office phone number (203) 555-0147
Should not have
• Colors outside of our logo colors + grey + black

```html
<!DOCTYPE html>
<html lang="en">
<head>
<meta charset="utf-8">
<title>Marwick Care Group – Letterhead</title>
<link rel="stylesheet" href="https://fonts.googleapis.com/css2?family=Open+Sans:wght@400;700&family=Lora:wght@500&display=swap">
<style>
  :root {
    --brand-blue: #4a7fe0;
    --brand-green: #00964a;
    --ink-grey: #3a3a3a;
    --icon-grey: #919191;
    --stage: #c8c7c8;
    --paper: #ffffff;
  }
  html, body { margin: 0; padding: 0; overflow: hidden; }
  body { width: 1000px; height: 1200px; background: var(--stage); }
  .letterhead-board { display: block; width: 1000px; height: 1200px; }
  .contact-text { font-family: "Open Sans", Arial, sans-serif; fill: var(--ink-grey); }
  .contact-web { font-size: 10.4px; }
  .contact-phone { font-family: "Lora", Georgia, serif; font-size: 11.2px; font-weight: 500; fill: var(--ink-grey); }
  .contact-address { font-size: 8.8px; }
  .brand-name { font-family: "Open Sans", Arial, sans-serif; font-weight: 700; fill: var(--brand-blue); }
  .brand-mark { fill: var(--brand-green); }
  .icon { fill: var(--icon-grey); }
  .icon-line { fill: none; stroke: var(--icon-grey); stroke-width: 1; }
  .swoosh-blue { fill: none; stroke: var(--brand-blue); stroke-width: 10; }
</style>
</head>
<body>
<svg class="letterhead-board" viewBox="0 0 1000 1200" xmlns="http://www.w3.org/2000/svg" role="img" aria-label="Marwick Care Group letterhead with enlarged header detail">
  <defs>
    <linearGradient id="green-fade-left" x1="0" y1="0" x2="1" y2="0">
      <stop offset="0" stop-color="#00964a" stop-opacity="0"/>
      <stop offset="0.7" stop-color="#00964a" stop-opacity="0.9"/>
      <stop offset="1" stop-color="#00964a"/>
    </linearGradient>
    <linearGradient id="grey-fade-left" x1="0" y1="0" x2="1" y2="0.3">
      <stop offset="0" stop-color="#d9d9d9" stop-opacity="0.2"/>
      <stop offset="1" stop-color="#9a9a9a"/>
    </linearGradient>
    <linearGradient id="green-fade-right" x1="0" y1="0" x2="1" y2="0">
      <stop offset="0" stop-color="#00964a" stop-opacity="0"/>
      <stop offset="1" stop-color="#00964a"/>
    </linearGradient>
    <linearGradient id="grey-fade-right" x1="1" y1="0" x2="0" y2="0.4">
      <stop offset="0" stop-color="#ffffff"/>
      <stop offset="0.6" stop-color="#a8a8a8"/>
      <stop offset="1" stop-color="#8a8a8a"/>
    </linearGradient>
    <linearGradient id="rule-fade" x1="0" y1="0" x2="1" y2="0">
      <stop offset="0" stop-color="#9a9a9a" stop-opacity="0"/>
      <stop offset="0.2" stop-color="#9a9a9a"/>
      <stop offset="0.8" stop-color="#9a9a9a"/>
      <stop offset="1" stop-color="#9a9a9a" stop-opacity="0"/>
    </linearGradient>
    <clipPath id="page-clip"><rect x="0" y="0" width="596" height="602"/></clipPath>
    <clipPath id="detail-clip"><rect x="0" y="782" width="1000" height="418"/></clipPath>

    <g id="header">
      <!-- left swoosh -->
      <path d="M0,30 C120,25 190,60 232,112 C170,72 80,62 0,92 Z" fill="url(#grey-fade-left)"/>
      <path d="M0,0 L100,0 C170,22 205,75 232,112 C190,60 120,25 0,30 Z" fill="url(#green-fade-left)"/>
      <!-- right swoosh -->
      <path d="M535,0 L596,0 L596,110 C585,170 540,215 460,234 C540,214 585,150 565,70 C556,40 548,20 535,0 Z" fill="url(#grey-fade-right)"/>
      <path d="M468,0 L528,0 C540,14 548,32 556,52 C530,25 500,8 468,0 Z" fill="url(#green-fade-right)"/>
      <path class="swoosh-blue" d="M95,0 C175,25 215,90 245,128 C300,195 370,240 445,236 C545,230 592,140 556,52 C548,32 540,14 530,0"/>
      <path d="M527,-2 L548,-2 C556,14 562,30 566,52 L556,52 C548,32 540,14 527,-2 Z" fill="var(--brand-blue)"/>

      <!-- divider rule -->
      <rect x="59" y="154" width="466" height="1.2" fill="url(#rule-fade)"/>

      <!-- brand -->
      <circle class="brand-mark" cx="129" cy="98" r="47"/>
      <text class="brand-name" x="47" y="181" font-size="17.5" textLength="164" lengthAdjust="spacingAndGlyphs">MARWICK</text>
      <text class="brand-name" x="47" y="196" font-size="10" textLength="164" lengthAdjust="spacing">CARE GROUP</text>

      <!-- contact: web -->
      <circle class="icon" cx="329" cy="52" r="5"/>
      <path d="M324,52 H334 M329,47 V57 M325.5,49 H332.5 M325.5,55 H332.5" stroke="#fff" stroke-width="0.7" fill="none"/>
      <text class="contact-text contact-web" x="342" y="55.5">www.marwickcaregroup.example</text>
      <!-- contact: email -->
      <rect class="icon" x="323" y="67" width="12" height="8" rx="0.8"/>
      <path d="M323,67 L329,72 L335,67" stroke="#fff" stroke-width="0.8" fill="none"/>
      <text class="contact-text contact-web" x="342" y="74.5">Info@Marwickcaregroup.example</text>
      <!-- contact: phone -->
      <circle class="icon-line" cx="329" cy="91" r="5.2"/>
      <path class="icon" d="M326.6,87.6 C325.6,88.6 326.3,91.5 328.3,93.4 C330.3,95.3 332.5,95.6 333,94.6 L331.8,93.2 L330.6,93.8 C329.5,93.2 328.5,92 328,90.8 L328.8,89.8 Z"/>
      <text class="contact-phone" x="342" y="95">(203) 555-0147</text>

      <!-- contact: Stamford office -->
      <path class="icon" d="M329,114 a4,4 0 0 1 4,4 c0,3 -4,7.5 -4,7.5 c0,0 -4,-4.5 -4,-7.5 a4,4 0 0 1 4,-4 Z"/>
      <circle cx="329" cy="118" r="1.4" fill="#fff"/>
      <text class="contact-text contact-address" x="342" y="121">
        <tspan x="342" dy="0">Marwick Care Group</tspan>
        <tspan x="342" dy="11.8">12 Linden Ave. Suite 310</tspan>
        <tspan x="342" dy="11.8">Stamford CT, 06900</tspan>
      </text>

      <!-- contact: New York office -->
      <path class="icon" d="M329,162 a4,4 0 0 1 4,4 c0,3 -4,7.5 -4,7.5 c0,0 -4,-4.5 -4,-7.5 a4,4 0 0 1 4,-4 Z"/>
      <circle cx="329" cy="166" r="1.4" fill="#fff"/>
      <text class="contact-text contact-address" x="342" y="169">
        <tspan x="342" dy="0">New York Office:</tspan>
        <tspan x="342" dy="11.8">88 Harlow St.</tspan>
        <tspan x="342" dy="11.8">New York, NY, 10000</tspan>
      </text>
    </g>
  </defs>

  <rect width="1000" height="1200" fill="var(--stage)"/>

  <!-- full page -->
  <g class="letterhead-page" transform="translate(201,178)">
    <rect width="596" height="602" fill="var(--paper)"/>
    <g clip-path="url(#page-clip)"><use href="#header"/></g>
  </g>

  <!-- enlarged header detail -->
  <g class="header-detail" clip-path="url(#detail-clip)">
    <rect x="0" y="782" width="1000" height="418" fill="var(--paper)"/>
    <use href="#header" transform="translate(0,782) scale(1.68)"/>
  </g>
</svg>
</body>
</html>
```